Antibacterial Hand Wash Squeeze Tube Label

We're looking for a contemporary label design for a new Antibacterial Hand Wash for an 8oz squeeze tube. The new consumer brand will be sold to consumers in major US retail stores & online. The moisturizing hand wash contains Aloe Vera, vitamin E, and other natural ingredients so the design should include the color green. Real photos are very effective on packaging, so a picture of Aloe Vera or possibly two hands washing would help draw consumers' attention to the tube on the retail shelf. The front label may wrap around the sides. Rear must be left mostly blank
Target Market(s)
US Consumers - retail stores & online
Industry/Entity Type
Consumer

```html
<!DOCTYPE html>
<html lang="en">
<head>
<meta charset="utf-8">
<title>Veridel Antibacterial Hand Sanitizer Label</title>
<link rel="stylesheet" href="https://fonts.googleapis.com/css2?family=Roboto+Condensed:wght@500;700&family=Montserrat:wght@400;600;700&display=swap">
<style>
  :root {
    --green: #1ea33a;
    --leaf: #6cbf2e;
    --leaf-light: #d7ecaa;
    --leaf-pale: #e9f5c9;
    --red: #d8211f;
    --blue: #1a8fd6;
    --ink: #1a1a1a;
    --pill-grey: #c9c9c9;
    --paper: #ffffff;
  }
  * { margin: 0; padding: 0; box-sizing: border-box; }
  html, body { width: 1200px; height: 737px; overflow: hidden; background: var(--paper); }
  .canvas { position: relative; width: 1200px; height: 737px; background: var(--paper); }
  .label {
    position: absolute; left: 441px; top: 48px; width: 318px; height: 640px;
    background: var(--paper); overflow: hidden; border-top-left-radius: 24px;
    font-family: 'Montserrat', sans-serif; text-align: center;
  }
  .label-art { position: absolute; inset: 0; }
  .photo-aloe-hands { position: absolute; }
  .brand {
    position: absolute; top: 34px; left: 0; right: 0;
    display: flex; justify-content: center; align-items: center; gap: 6px;
    font-family: 'Roboto Condensed', sans-serif; font-weight: 500; font-size: 20px;
    color: var(--blue); letter-spacing: 0.2px;
  }
  .brand-mark { width: 14px; height: 14px; border-radius: 50%; background: var(--blue); }
  .descriptor {
    position: absolute; top: 110px; left: 0; right: 0;
    font-size: 17px; font-weight: 400; letter-spacing: 4.2px; color: var(--green);
  }
  .product-name {
    position: absolute; top: 128px; left: 0; right: 0;
    font-family: 'Roboto Condensed', sans-serif; font-weight: 700; color: var(--green);
    font-size: 52px; line-height: 44px; letter-spacing: -1px;
  }
  .pill {
    position: absolute; top: 222px; left: 62px; width: 195px; height: 23px; border-radius: 6px;
    background: linear-gradient(90deg, var(--pill-grey), #f2f2f2 45%, #f2f2f2 60%, var(--pill-grey));
    font-weight: 700; font-size: 14px; line-height: 23px; color: var(--ink); letter-spacing: 0.4px;
  }
  .ingredients {
    position: absolute; top: 262px; left: 0; right: 0; color: var(--leaf);
    font-family: 'Roboto Condensed', sans-serif; font-weight: 700; font-size: 18px; line-height: 18px;
  }
  .ingredients small { display: block; font-family: 'Montserrat', sans-serif; font-size: 7px; line-height: 14px; font-weight: 600; letter-spacing: 0.2px; }
  .claim { position: absolute; top: 342px; left: 0; right: 0; color: var(--red); font-weight: 700; }
  .claim-kills { font-size: 21px; line-height: 24px; }
  .claim-figure { font-size: 36px; line-height: 36px; }
  .claim-germs { font-size: 21px; line-height: 24px; }
  .net-content {
    position: absolute; bottom: 18px; left: 160px; width: 140px; text-align: center;
    font-weight: 700; font-size: 14px; color: var(--paper);
  }
</style>
</head>
<body>
<main class="canvas">
  <section class="label">
    <svg class="label-art" width="318" height="640" viewBox="0 0 318 640" aria-hidden="true">
      <defs>
        <linearGradient id="swoosh" x1="0" y1="0" x2="1" y2="0">
          <stop offset="0" stop-color="#c9c9c9"/>
          <stop offset="1" stop-color="#ffffff"/>
        </linearGradient>
        <linearGradient id="band" x1="0" y1="0" x2="1" y2="0">
          <stop offset="0" stop-color="#6cbf2e"/>
          <stop offset="0.7" stop-color="#8ccd4a"/>
          <stop offset="1" stop-color="#d7ecaa"/>
        </linearGradient>
      </defs>
      <path d="M0 0 H212 C140 10 50 40 0 72 Z" fill="#6cbf2e"/>
      <path d="M0 86 C40 50 120 15 210 0 C130 20 50 55 6 96 Z" fill="url(#swoosh)"/>
      <path d="M0 445 C110 480 230 460 318 400 V640 H0 Z" fill="url(#band)"/>
      <path d="M0 468 C110 500 230 480 318 420 V640 H0 Z" fill="#d7ecaa"/>
      <path d="M0 482 C110 512 230 492 318 432 V640 H0 Z" fill="#e2f1b8"/>
      <path d="M0 545 C120 575 240 560 318 530 V640 H0 Z" fill="#cfe89a"/>
    </svg>
    <svg class="photo-aloe-hands" style="left:60px;top:290px" width="258" height="320" viewBox="0 0 258 320" role="img" aria-label="Photo of aloe vera leaves and slices beside two hands rubbing together">
      <defs>
        <radialGradient id="photoTone" cx="0.65" cy="0.65" r="0.6">
          <stop offset="0" stop-color="#8fcf4c" stop-opacity="0.75"/>
          <stop offset="0.6" stop-color="#b8df7a" stop-opacity="0.45"/>
          <stop offset="1" stop-color="#e9f5c9" stop-opacity="0"/>
        </radialGradient>
      </defs>
      <rect width="258" height="320" fill="url(#photoTone)"/>
    </svg>
    <div class="brand"><span class="brand-mark"></span>VERIDEL</div>
    <div class="descriptor">ANTIBACTERIAL</div>
    <h1 class="product-name">HAND<br>SANITIZER</h1>
    <div class="pill">MOISTURIZING</div>
    <div class="ingredients">ALOE VERA<br>VITAMIN E<small>OTHER NATURAL INGREDIENTS</small></div>
    <div class="claim">
      <div class="claim-kills">KILLS</div>
      <div class="claim-figure">99.9%</div>
      <div class="claim-germs">OF GERMS</div>
    </div>
    <div class="net-content">8 FL OZ (246 mL)</div>
  </section>
</main>
</body>
</html>
```